Starter & Alternator business needs a website

update: very good designs submitted so far. also need this to display well on mobile devices. not sure if wordpress or html/css is better for my needs.

Our existing website is vellumtorq.com and is need of total revamp. Need full design of a website for my business.

We sell and rebuild starters and alternators. Customers bring in the units and we rebuild them. Or we sell them brand new or rebuilt units we have in stock. We do not install units into vehicles like a mechanic would. We strictly rebuild starters and alternators in our shop, sell brand new units over the counter, and we do deliver occasionally as well. We do offer a line of Orvan batteries as well but that is only a small feature of the business.

I would like this website designed and coded. I can upload the files to my web host after completion. I can also add in and modify content like our background info, etc.

I have included an illustrator file that shows some of our signage and logo, etc. I have also included a radio commercial sample so you can get a little better feel for the business. A similar ad does run on the radio currently, slightly different and without the added sound effects.

Update: I do like using photos of real items(starters or alternators etc) for an icon, like a real alternator stock image for the alternator section icon, etc. Maybe incorporate our logo in that design as well. That looks nice as well and may aid in navigation.

For any other design elements, do what you think looks good. Our colors are red/white/blue as seen in the illustrator file. our building is painted with halbeck moray colors, ember gala red and deep tide for blue.

Here are some examples of rebuilders websites in other markets for reference:

https://quillmarauto.com/starter-alternator-rebuilding/

https://www.dunwickmotorworks.com/auto-repairs/alternator-starter-rebuilds.aspx

https://www.fjordvoltage.com/

https://www.pemberlowgx.com/

The website can have areas for: services and products offered, high output alternators, Orvan Batteries, troubleshooting tips, current specials, contact info and directions/map, etc. Whatever else you feel applies.

At some point I do want to be able to sell items directly online or at least have a secure section for customers to submit invoice payments, but that's not necessarily in scope for this project just something to keep in mind.

Target Market(s)

Mechanics and Managers in fleet shops, construction and marine industries, shipping trades. Also automobile owners who work on their own vehicles. We sell and rebuild starters and alternators for automobiles, heavy duty equipment, forklifts, traxlifts, man movers, ferrettes, loaders, large tractors and trucks, just about any engine, golf carts, generators, etc.

Industry/Entity Type

Automotive Part

Coding

Coded - Design and coding required

Number of Pages Required

5+ page

Font styles to use
Serif
Sans Serif

Colors
0255a3
ec1f27
ffffff

Requirements
Must have
• Should also display nicely on mobile phones. Highlight our specialty, "Starters & Alternators"

```html
<!DOCTYPE html>
<html lang="en">
<head>
<meta charset="utf-8">
<title>Harrow Rebuild Co. | Starters &amp; Alternators</title>
<link rel="stylesheet" href="https://fonts.googleapis.com/css2?family=Roboto:wght@300;400;500;700&family=Roboto+Slab:wght@400;700&family=Lato:ital,wght@0,400;0,700;1,400&family=Poppins:wght@600&family=Noto+Serif&display=swap">
<style>
:root{
  --blue:#0255a3;
  --blue-bright:#0a66f0;
  --red:#ec1f27;
  --red-deep:#b5121a;
  --white:#ffffff;
  --ink:#222222;
  --muted:#8a8a8a;
  --dark:#1b1c1e;
  --darker:#161719;
  --hero:#141414;
}
*{box-sizing:border-box;margin:0;padding:0}
html,body{width:1200px;height:2773px;overflow:hidden;background:var(--white);font-family:'Lato',sans-serif;color:var(--ink)}
.page{position:relative;width:1200px;height:2773px}
.abs{position:absolute}
h1,h2,h3,h4{font-weight:400}

/* header */
.site-header{top:0;left:0;width:1200px;height:137px;background:var(--white)}
.brand{left:72px;top:24px;width:290px}
.brand-row{display:flex;align-items:center;gap:12px}
.brand-dot{width:22px;height:22px;border-radius:50%;background:var(--red);flex:none}
.brand-name{font-family:'Roboto',sans-serif;font-weight:700;font-size:30px;line-height:34px;color:var(--blue);white-space:nowrap}
.brand-phone{margin-top:12px;font-family:'Roboto',sans-serif;font-weight:500;font-size:22px;line-height:26px;color:var(--red)}
.brand-tag{margin-top:8px;font-family:'Roboto',sans-serif;font-weight:500;font-size:10px;color:var(--ink)}
.top-links{right:162px;top:29px;font-family:'Roboto',sans-serif;font-size:12.5px;color:var(--ink)}
.top-links span{margin:0 6px;color:#888}
.best-tab{left:755px;top:78px;width:325px;height:59px}
.best-tab svg{position:absolute;left:0;top:0}
.best-tab p{position:absolute;left:0;top:0;width:325px;height:59px;line-height:59px;text-align:center;color:var(--white);font-family:'Roboto',sans-serif;font-weight:300;font-size:40px;transform:scaleX(.82)}

/* hero */
.hero{top:137px;left:0;width:1200px;height:511px;background:var(--hero);overflow:hidden}
.hero-texture{left:0;top:0;width:1200px;height:511px}
.hero-products{left:70px;top:70px;width:560px;height:390px;border-radius:40px;background:radial-gradient(ellipse at center,#c9cbcf 0%,#8e9196 55%,rgba(60,60,62,0) 75%)}
.hero-title{left:700px;top:115px;width:410px;text-align:center;font-family:'Roboto',sans-serif;font-weight:300;color:var(--white);font-size:60px;line-height:71px;letter-spacing:1px}
.hero-sub{left:700px;top:362px;width:410px;text-align:center;font-family:'Lato',sans-serif;font-style:italic;font-size:16px;color:var(--red)}

/* main nav */
.main-nav{top:648px;left:0;width:1200px;height:57px;background:var(--blue);display:flex;padding-left:55px}
.main-nav a{font-family:'Roboto',sans-serif;font-weight:300;font-size:13.5px;color:var(--white);text-decoration:none;line-height:57px;padding:0 17px;border-right:1px solid rgba(255,255,255,.35);text-transform:uppercase;white-space:nowrap}
.main-nav a:last-child{border-right:0}
.main-nav a.active{background:var(--red);padding:0 11px}

/* about */
.about-label{left:101px;top:757px;font-family:'Roboto',sans-serif;font-size:13px;color:var(--ink)}
.about-label::after{content:"";display:block;width:20px;height:2px;background:var(--blue);margin-top:8px}
.about-photo{left:95px;top:797px;width:413px;height:278px;background:linear-gradient(135deg,#2a4a86 0%,#3b3d44 45%,#1c1d20 100%)}
.about-title{left:580px;top:748px;width:490px;font-family:'Roboto Slab',serif;font-weight:700;font-size:25px;line-height:31px;color:var(--blue)}
.about-lead{left:580px;top:834px;width:520px;font-style:italic;font-size:15px;color:#555}
.about-body{left:580px;top:864px;width:515px;font-size:14.5px;line-height:25.5px;color:#888;text-align:justify}
.btn-red{left:580px;top:1033px;width:109px;height:42px;background:var(--red);color:var(--white);font-family:'Roboto',sans-serif;font-size:12.5px;line-height:42px;text-align:center;border:1px solid #ff8d92}

/* services */
.services{top:1133px;left:0;width:1200px;height:388px;background:linear-gradient(90deg,var(--red-deep) 0%,#d01820 50%,var(--red) 100%)}
.section-title-light{top:1161px;left:0;width:1200px;text-align:center;font-family:'Roboto',sans-serif;font-weight:400;font-size:23px;color:var(--white)}
.section-title-light::after{content:"";display:block;width:20px;height:2px;background:rgba(255,255,255,.7);margin:10px auto 0}
.service{top:1226px;width:300px;text-align:center;color:var(--white)}
.service-icon{width:114px;height:114px;margin:0 auto;border-radius:50%;background:var(--white);border:3px dotted rgba(255,255,255,.8);outline:6px solid rgba(255,255,255,.35);display:flex;align-items:center;justify-content:center}
.service-icon i{display:block;width:70px;height:70px;border-radius:50%;background:radial-gradient(circle,#9a9ca1 0%,#4a4b4f 80%)}
.service h3{margin-top:30px;font-family:'Roboto Slab',serif;font-weight:700;font-size:23px}
.service p{margin-top:10px;font-size:13px;line-height:20px}
.service a{display:inline-block;margin-top:18px;font-size:13px;color:var(--white);text-decoration:underline}

/* posts */
.news{top:1521px;left:0;width:1200px;height:516px;background:linear-gradient(180deg,#ececec 0%,#f6f6f6 50%,#e3e3e3 100%)}
.section-title-dark{top:1580px;left:0;width:1200px;text-align:center;font-family:'Roboto',sans-serif;font-weight:400;font-size:23px;color:var(--ink)}
.section-title-dark::after{content:"";display:block;width:20px;height:2px;background:var(--blue);margin:10px auto 0}
.news-card{top:1647px;left:72px;width:1051px;height:338px;background:var(--white)}
.post{top:1670px;width:290px;text-align:center}
.post time{font-family:'Noto Serif',serif;font-size:11px;color:#333}
.post h4{margin-top:8px;font-family:'Poppins',sans-serif;font-weight:600;font-size:24px;line-height:31px;letter-spacing:-.6px;color:#111}
.post p{margin:8px auto 0;width:270px;font-family:'Noto Serif',serif;font-size:15px;line-height:28px;color:#777}
.dots{top:1945px;left:584px;display:flex;gap:12px}
.dots i{width:8px;height:8px;border-radius:50%;background:#c9c9c9}

/* contact */
.stripe{top:2052px;left:0;width:1200px;height:16px;background:var(--blue-bright)}
.contact{top:2068px;left:0;width:1200px;height:492px;background:var(--dark)}
.contact-label{top:2120px;left:0;width:1200px;text-align:center;font-family:'Roboto',sans-serif;font-size:10px;letter-spacing:4px;color:var(--blue-bright)}
.contact-title{top:2166px;left:0;width:1200px;text-align:center;font-family:'Roboto Slab',serif;font-weight:700;font-size:28px;color:var(--white)}
.contact-text{top:2220px;left:350px;width:500px;text-align:center;font-family:'Noto Serif',serif;font-size:16px;line-height:28px;color:#8d8d8d}
.field{width:325px;height:52px;background:var(--white);font-family:'Noto Serif',serif;font-size:15px;color:#555;line-height:52px;padding-left:26px}
.btn-blue{top:2463px;left:476px;width:274px;height:47px;background:var(--blue-bright);color:var(--white);font-family:'Roboto',sans-serif;font-weight:700;font-size:12.5px;letter-spacing:1.4px;line-height:47px;text-align:center}
.footer{top:2560px;left:0;width:1200px;height:213px;background:var(--darker)}
.social{top:2662px;left:532px;display:flex;gap:26px}
.social i{width:12px;height:12px;border-radius:50%;background:var(--white)}
</style>
</head>
<body>
<div class="page">

  <header class="site-header abs">
    <div class="brand abs">
      <div class="brand-row"><span class="brand-dot"></span><div class="brand-name">Harrow Rebuild Co.</div></div>
      <div class="brand-phone">472-6630</div>
      <div class="brand-tag">Automotive / Marine / Heavy Duty &nbsp; 2710 Harrow Blvd</div>
    </div>
    <nav class="top-links abs">Home<span>|</span>About Us<span>|</span>Contact info</nav>
    <div class="best-tab abs">
      <svg width="325" height="59" viewBox="0 0 325 59"><polygon points="12,0 325,0 313,59 0,59" fill="#0255a3"/></svg>
      <p>BEST SUPPLIERS</p>
    </div>
  </header>

  <section class="hero abs">
    <svg class="hero-texture abs" width="1200" height="511" viewBox="0 0 1200 511">
      <defs>
        <pattern id="mesh" width="12" height="12" patternUnits="userSpaceOnUse">
          <rect width="12" height="12" fill="#202123"/>
          <circle cx="6" cy="6" r="4" fill="#2e2f32"/>
        </pattern>
      </defs>
      <polygon points="0,0 740,0 690,511 0,511" fill="url(#mesh)"/>
      <line x1="740" y1="0" x2="690" y2="511" stroke="#555" stroke-width="2"/>
    </svg>
    <div class="hero-products abs" role="img" aria-label="Product photo of a silver starter motor and an alternator"></div>
    <h1 class="hero-title abs">STARTERS<br>&amp;<br>ALTERNATORS</h1>
    <p class="hero-sub abs">Automotive &nbsp;/ &nbsp;Marine &nbsp;/ &nbsp;Heavy Duty</p>
  </section>

  <nav class="main-nav abs">
    <a class="active">Services &amp; Products Offered</a>
    <a>High Output Alternators</a>
    <a>Orvan Batteries</a>
    <a>Troubleshooting Tips</a>
    <a>Current Specials</a>
    <a>Blogs</a>
  </nav>

  <section class="about">
    <p class="about-label abs">WHO WE ARE</p>
    <div class="about-photo abs" role="img" aria-label="Photo of mechanics giving thumbs up over an engine bay"></div>
    <h2 class="about-title abs">Your source for New and Hight-Quality<br>Rebuilt Starters &amp; Alternators</h2>
    <p class="about-lead abs">Serving the Marine, Heavy Duty, Specialty, and Automotive industries.</p>
    <p class="about-body abs">It is a long established fact that a reader will be distracted by the readable content of a page when looking at its layout. The point of using Lorem Ipsum is that it has a more-or-less normal distribution of letters, as opposed to using 'Content here, content here', making it look like readable English. Many desktop publishing packages and web page editors now use Lorem Ipsum as their default model text.</p>
    <div class="btn-red abs">KNOW MORE</div>
  </section>

  <section class="services abs" role="img" aria-label="Red tinted photo of a technician working on a motor"></section>
  <h2 class="section-title-light abs">SERVICES &amp; PRODUCTS OFFERED</h2>
  <div class="service abs" style="left:68px">
    <div class="service-icon"><i role="img" aria-label="Alternator product photo"></i></div>
    <h3>Alternators</h3>
    <p>Lorem Ipsum is simply dummy text of<br>the printing and typesetting industry.</p>
    <a>Read More...</a>
  </div>
  <div class="service abs" style="left:430px">
    <div class="service-icon"><i role="img" aria-label="Starter motor product photo"></i></div>
    <h3>Starters</h3>
    <p>Lorem Ipsum is simply dummy text of<br>the printing and typesetting industry.</p>
    <a>Read More...</a>
  </div>
  <div class="service abs" style="left:768px">
    <div class="service-icon"><i role="img" aria-label="Battery product photo"></i></div>
    <h3>Orvan Batteries</h3>
    <p>Lorem Ipsum is simply dummy text of<br>the printing and typesetting industry.</p>
    <a>Read More...</a>
  </div>

  <section class="news abs" role="img" aria-label="Faded background photo of alternator parts"></section>
  <h2 class="section-title-dark abs">RECENT POST AND NEWS</h2>
  <div class="news-card abs"></div>
  <article class="post abs" style="left:112px">
    <time>March 25, 2017</time>
    <h4>We are nominated to Agency of Year for the second time</h4>
    <p>Many years ago, I worked for my parents who own a video production company. Because it is a family business, you...</p>
  </article>
  <article class="post abs" style="left:456px">
    <time>March 22, 2017</time>
    <h4>Can your business become better with new technology?</h4>
    <p>Last year I wrote about why booking too far in advance can be dangerous for your business, and this concept of margin...</p>
  </article>
  <article class="post abs" style="left:798px">
    <time>March 20, 2017</time>
    <h4>How collaborative teams create meaningful things</h4>
    <p>Just the other day I happened to wake up early. That is unusual for an engineering student. After a long time I could...</p>
  </article>
  <div class="dots abs"><i></i><i></i></div>

  <div class="stripe abs"></div>
  <section class="contact abs"></section>
  <p class="contact-label abs">CONTACT</p>
  <h2 class="contact-title abs">Talk to us about our services</h2>
  <p class="contact-text abs">Our core clients are from the Europe countries, but we are happy to work with clients from all over the globe.</p>
  <div class="field abs" style="left:280px;top:2308px">Full Name *</div>
  <div class="field abs" style="left:621px;top:2308px">Company *</div>
  <div class="field abs" style="left:280px;top:2378px">Email *</div>
  <div class="field abs" style="left:621px;top:2378px">Telephone *</div>
  <div class="btn-blue abs">SUBMIT US YOUR REQUEST</div>

  <footer class="footer abs"></footer>
  <div class="social abs"><i></i><i></i><i></i><i></i><i></i></div>

</div>
</body>
</html>
```